Global Expert Network Firm needs business card design

We need business card design for a new company based in Seoul, South Korea called 'Corwell Insight Partners'. We recruit industry experts covering all countries and connect our client and recruited expert by phone, face-to-face meetings and etc. We are a global expert network firm that is focused on delivering high-quality experts to our clients throughout the world. Our clients include multinational corporations, global consulting firms, private equity firms, venture capital firms, asset management companies.
We have made new logo and please find attachment.(Please use new logo)
Target Market(s)
Global Consulting Firms, Investment Firms, Private Equity Firms, Venture Capital Firms.
Industry/Entity Type
Recruitment
Contact Information for Business Card
We need two Languages (English and Korean Version).
The front is Korean and the back is English version.
[The back] [English]
Company Name: Corwell Insight Partners, Inc.
CEO Name: Daniel Park
Address: #507, Hanbit Bldg, 82 Maebongsan-ro, Dobong-gu, Seoul, 01327, Korea
Tel. +82 2 718 4052
Fax. +82 2 864 1097
Mobile. +82 10 7264 8815
Email: daniel@corwellip.com
Web: www.corwellip.com
[The front] [Korean] => Described in same order as English version.
회사명: 코웰인사이트파트너스(주)
대표이사: 박도현
주소: 서울시 도봉구 매봉산로 82 한빛빌딩 507호
Tel. 02 718 4052
Fax. 02 864 1097
Mobile. 010 7264 8815
Web: www.corwellip.com
Look and feel
Each slider illustrates characteristics of the customer's brand and the style your logo design should communicate.

```html
<!DOCTYPE html>
<html lang="en">
<head>
<meta charset="utf-8">
<title>Corwell Insight Partners – Business Card</title>
<link href="https://fonts.googleapis.com/css2?family=Montserrat:wght@400;500&family=Roboto:wght@400;500;700&display=swap" rel="stylesheet">
<style>
  :root {
    --paper: #efeeea;
    --navy: #1e2650;
    --trim: #3a3a3a;
  }
  * { margin: 0; padding: 0; box-sizing: border-box; }
  html, body { width: 720px; height: 1200px; overflow: hidden; background: var(--paper); }
  .card { position: relative; width: 720px; height: 1200px; background: var(--paper); color: var(--navy); }

  .crop-marks { position: absolute; inset: 0; }

  .brand { position: absolute; left: 127px; top: 150px; display: flex; align-items: flex-start; gap: 18px; }
  .brand-square { width: 52px; height: 52px; background: var(--navy); flex: none; }
  .brand-name {
    font-family: "Montserrat", sans-serif; font-weight: 500; font-size: 30px;
    line-height: 38px; letter-spacing: 1.5px; text-transform: uppercase; color: var(--navy);
  }

  .person { position: absolute; left: 129px; top: 620px; }
  .person-name {
    font-family: "Roboto", sans-serif; font-weight: 700; font-size: 43px;
    letter-spacing: 2.5px; line-height: 1; text-transform: uppercase;
  }
  .person-title {
    margin-top: 13px; margin-left: -1px; font-family: "Roboto", sans-serif; font-weight: 400; font-size: 27px;
    letter-spacing: 1.6px; line-height: 1; text-transform: uppercase;
  }
  .divider { position: absolute; left: 130px; top: 726px; width: 36px; height: 4px; background: var(--navy); }

  .address {
    position: absolute; left: 131px; top: 762px; font-style: normal;
    font-family: "Montserrat", sans-serif; font-weight: 400; font-size: 25px; line-height: 36px;
  }

  .contacts { position: absolute; left: 126px; top: 900px; list-style: none; }
  .contact {
    display: flex; align-items: center; height: 45.5px;
    font-family: "Montserrat", sans-serif; font-weight: 400; font-size: 26px;
  }
  .contact-icon { width: 28px; height: 28px; margin-right: 20px; fill: var(--navy); flex: none; }
</style>
</head>
<body>
<main class="card">
  <svg class="crop-marks" width="720" height="1200" viewBox="0 0 720 1200" aria-hidden="true">
    <g stroke="var(--trim)" stroke-width="1">
      <line x1="40.5" y1="0" x2="40.5" y2="23"/>
      <line x1="680.5" y1="0" x2="680.5" y2="23"/>
      <line x1="0" y1="38.5" x2="27" y2="38.5"/>
      <line x1="696" y1="38.5" x2="720" y2="38.5"/>
      <line x1="40.5" y1="1177" x2="40.5" y2="1200"/>
      <line x1="680.5" y1="1177" x2="680.5" y2="1200"/>
      <line x1="0" y1="1157.5" x2="27" y2="1157.5"/>
      <line x1="696" y1="1157.5" x2="720" y2="1157.5"/>
    </g>
  </svg>

  <header class="brand">
    <span class="brand-square" aria-hidden="true"></span>
    <span class="brand-name">Corwell<br>Insight<br>Partners</span>
  </header>

  <section class="person">
    <h1 class="person-name">Daniel Park</h1>
    <p class="person-title">Founder &amp; CEO</p>
  </section>
  <div class="divider" aria-hidden="true"></div>

  <address class="address">
    #507, Hanbit Bldg, 82<br>
    Maebongsan-ro, Dobong-gu,<br>
    Seoul, 01327, Korea
  </address>

  <ul class="contacts">
    <li class="contact">
      <svg class="contact-icon" viewBox="0 0 28 28" aria-label="Telephone"><path d="M3 11c0-4 5-6 11-6s11 2 11 6v2h-6v-3c-2-.6-8-.6-10 0v3H3z"/><path d="M8 13h12l4 9H4z"/></svg>
      <span>02 718 4052</span>
    </li>
    <li class="contact">
      <svg class="contact-icon" viewBox="0 0 28 28" aria-label="Fax"><rect x="8" y="4" width="12" height="5"/><rect x="3" y="10" width="22" height="10" rx="2"/><rect x="8" y="17" width="12" height="7" fill="var(--paper)" stroke="var(--navy)" stroke-width="2"/></svg>
      <span>02 864 1097</span>
    </li>
    <li class="contact">
      <svg class="contact-icon" viewBox="0 0 28 28" aria-label="Mobile"><rect x="7" y="2" width="14" height="24" rx="2"/><rect x="9" y="5" width="10" height="16" fill="var(--paper)"/><circle cx="14" cy="23.5" r="1.2" fill="var(--paper)"/></svg>
      <span>010 7264 8815</span>
    </li>
    <li class="contact">
      <svg class="contact-icon" viewBox="0 0 28 28" aria-label="Email"><rect x="3" y="7" width="22" height="15"/><path d="M4 8l10 8 10-8" fill="none" stroke="var(--paper)" stroke-width="2"/></svg>
      <span>daniel@corwellip.com</span>
    </li>
    <li class="contact">
      <svg class="contact-icon" viewBox="0 0 28 28" aria-label="Website"><rect x="3" y="5" width="22" height="15" rx="1"/><rect x="5.5" y="7.5" width="17" height="10" fill="var(--paper)"/><rect x="12" y="20" width="4" height="3"/><rect x="9" y="23" width="10" height="2"/></svg>
      <span>www.corwellip.com</span>
    </li>
  </ul>
</main>
</body>
</html>
```